Healthcare IT firm needs classy and unique business care design

We need a business card design that incorporates our new logo design (attached) Prefer a purple based designed. I would really love to see something utilizing the "3D" version of the logo (purple on the reflective wall). I want something a little more than my logo printed along with a person's detailed contact information.
Contact Information for Business Card
Want something polished, professional, and a little unique in the design.
Colors
6b449b
Requirements
Must have
- Please use similar font as the logo design
Nice to have
- Would like to see the 3d version of my logo incorporated into the design.

```html
<!DOCTYPE html>
<html lang="en">
<head>
<meta charset="utf-8">
<title>Kindwell Care Systems — Business Card</title>
<link rel="stylesheet" href="https://fonts.googleapis.com/css2?family=Arimo:wght@400;700&display=swap">
<style>
  :root {
    --brand-purple: #6b449b;
    --card-white: #f4f4f4;
    --edge-shadow: #444444;
    --ink: #111111;
    --canvas-bg: #2a2a2a;
    --on-purple: #ffffff;
    --faint-mark: rgba(255, 255, 255, 0.06);
  }
  * { box-sizing: border-box; margin: 0; padding: 0; }
  html, body { width: 1200px; height: 1000px; overflow: hidden; }
  body {
    background: var(--canvas-bg);
    font-family: "Arimo", Arial, sans-serif;
    position: relative;
  }
  .card {
    position: absolute;
    left: 253px;
    width: 697px;
    height: 418px;
    border-radius: 14px;
    overflow: hidden;
  }
  .card--front { top: 50px; background: var(--card-white); }
  .card--back { top: 531px; background: var(--brand-purple); }

  .front-shape { position: absolute; inset: 0; }

  .owner {
    position: absolute;
    left: 31px;
    top: 21px;
    color: var(--on-purple);
    text-align: center;
  }
  .owner__name { font-size: 20px; font-weight: 400; letter-spacing: 0.2px; }
  .owner__role { font-size: 11px; margin-top: 2px; }

  .company-name {
    position: absolute;
    left: 124px;
    top: 170px;
    width: 196px;
    color: var(--brand-purple);
    font-weight: 700;
    text-align: center;
    line-height: 1;
  }
  .company-name__main { display: block; font-size: 42px; letter-spacing: -1px; }
  .company-name__sub { display: block; font-size: 12px; letter-spacing: 0.6px; margin-top: 6px; }

  .divider {
    position: absolute;
    left: 346px;
    top: 143px;
    width: 2px;
    height: 127px;
    background: var(--ink);
  }

  .contact-list {
    position: absolute;
    left: 364px;
    top: 152px;
    list-style: none;
  }
  .contact-list__item {
    display: flex;
    align-items: center;
    height: 18px;
    margin-bottom: 10px;
    font-size: 13px;
    color: var(--ink);
  }
  .contact-list__item:first-child { margin-bottom: 16px; }
  .contact-list__icon {
    width: 18px;
    height: 18px;
    margin-right: 18px;
    fill: var(--brand-purple);
    flex: none;
  }

  .back-watermark-name {
    position: absolute;
    left: 0;
    right: 0;
    top: 118px;
    text-align: center;
    color: var(--faint-mark);
    font-weight: 700;
    line-height: 1;
  }
  .back-watermark-name__main { display: block; font-size: 150px; letter-spacing: -4px; }
  .back-watermark-name__sub { display: block; font-size: 40px; letter-spacing: 2px; margin-top: 6px; }

  .back-name {
    position: absolute;
    left: 0;
    right: 0;
    top: 168px;
    text-align: center;
    color: var(--on-purple);
    font-weight: 700;
    line-height: 1;
  }
  .back-name__main { display: block; font-size: 64px; letter-spacing: -1.5px; }
  .back-name__sub { display: block; font-size: 17px; letter-spacing: 1px; margin-top: 8px; }
</style>
</head>
<body>

<section class="card card--front" aria-label="Business card front">
  <svg class="front-shape" width="697" height="418" viewBox="0 0 697 418" aria-hidden="true">
    <path d="M0 0 H697 V38 H392 Q370 38 368 56 Q366 76 344 76 H0 Z" fill="var(--brand-purple)"/>
    <path d="M0 76 H344 Q366 76 368 56 Q370 38 392 38 H697" fill="none" stroke="var(--edge-shadow)" stroke-width="3"/>
    <path d="M0 418 H697 V343 H362 Q340 343 338 362 Q336 382 314 382 H0 Z" fill="var(--brand-purple)"/>
    <path d="M0 382 H314 Q336 382 338 362 Q340 343 362 343 H697" fill="none" stroke="var(--edge-shadow)" stroke-width="3"/>
  </svg>

  <div class="owner">
    <p class="owner__name">NAME OF OWNER</p>
    <p class="owner__role">DESIGNATION</p>
  </div>

  <p class="company-name">
    <span class="company-name__main">Kindwell</span>
    <span class="company-name__sub">CARE SYSTEMS</span>
  </p>

  <div class="divider"></div>

  <ul class="contact-list">
    <li class="contact-list__item">
      <svg class="contact-list__icon" viewBox="0 0 24 24" aria-hidden="true"><path d="M12 1a8 8 0 0 0-8 8c0 6 8 14 8 14s8-8 8-14a8 8 0 0 0-8-8zm0 11a3 3 0 1 1 0-6 3 3 0 0 1 0 6z"/></svg>
      Your city address, Street location
    </li>
    <li class="contact-list__item">
      <svg class="contact-list__icon" viewBox="0 0 24 24" aria-hidden="true"><path d="M6.6 2.5l2.6 4-1.8 2.2c1 2.6 3.2 5.2 5.8 6.6l2-1.7 4 2.6-1.4 3.6c-7.4.4-14.6-8.4-13-16z"/></svg>
      0123456789
    </li>
    <li class="contact-list__item">
      <svg class="contact-list__icon" viewBox="0 0 24 24" aria-hidden="true"><path d="M2 5h20v14H2zM3.5 6.5l8.5 7 8.5-7" fill="var(--brand-purple)" stroke="var(--card-white)" stroke-width="1.4"/></svg>
      info@companyname.com
    </li>
    <li class="contact-list__item">
      <svg class="contact-list__icon" viewBox="0 0 24 24" aria-hidden="true"><circle cx="12" cy="12" r="10"/><path d="M2 12h20M12 2c-4 5-4 15 0 20M12 2c4 5 4 15 0 20M4 7h16M4 17h16" fill="none" stroke="var(--card-white)" stroke-width="1.2"/></svg>
      www.companyname.com
    </li>
  </ul>
</section>

<section class="card card--back" aria-label="Business card back">
  <p class="back-watermark-name" aria-hidden="true">
    <span class="back-watermark-name__main">Kindwell</span>
    <span class="back-watermark-name__sub">CARE SYSTEMS</span>
  </p>
  <p class="back-name">
    <span class="back-name__main">Kindwell</span>
    <span class="back-name__sub">CARE SYSTEMS</span>
  </p>
</section>

</body>
</html>
```